Tree company needs modern website design

We need a website design for a tree company, here are some websites they like:

http://korvalemarine.com/company/ - we like the big image filling most of the page. Also the top half of the page looks good with the logo along top and good task bar also (we don’t like the spiel on left hand side covering up the picture + too many words!) If we could have our logo at lop like this along with our slogan which is 'Great Looking Trees that Grow Well'

http://www.pinecroftgardens.co.nz/ - we like the bottom half of this with the clean lines and welcome to part down bottom rather than the spiel to the left as on above site. Also like the moving leaves, any chance we could have birds such as a fantail, Tui and Bellbirds flying across the page and also some birdsong playing?

This is their existing website, that needs an updated design: http://tallfernwood.co.nz/

Industry/Entity Type

It Company

Font styles to use
Serif
Sans Serif

Requirements
Must have
• "Website by Pages Built Simple" located in bottom right hand side
Use images provided as background or banner images
Should not have
• Social Media icons

```html
<!DOCTYPE html>
<html lang="en">
<head>
<meta charset="utf-8">
<title>Tall Fern Trees</title>
<link href="https://fonts.googleapis.com/css2?family=Open+Sans:wght@400;600;700&family=Roboto:wght@400;500&display=swap" rel="stylesheet">
<style>
:root{
  --topbar:#3a3a3a;
  --cream:#fdfbe2;
  --ink:#222;
  --body:#444;
  --gold:#d8b400;
  --gold-btn:#e6c200;
  --teal:#0d7a78;
  --rule:#e4e4e4;
  --footer:#474747;
  --footer-base:#353535;
  --footer-text:#d6d6d6;
  --orange:#f19a1b;
  --brand:#1f5c22;
}
*{box-sizing:border-box;margin:0;padding:0}
html,body{width:836px;height:1200px;overflow:hidden}
body{position:relative;font-family:'Open Sans',sans-serif;color:var(--body);
  background:linear-gradient(to bottom,var(--cream) 0,var(--cream) 300px,#fff 340px)}
.abs{position:absolute}
.topbar{left:0;top:0;width:836px;height:36px;background:linear-gradient(#4a4a4a,#2c2c2c)}
.topbar .call{left:119px;top:11px;font-size:8.5px;color:#eee;display:flex;align-items:center;gap:6px}
.search{left:587px;top:7px;width:130px;height:21px;background:#fff;border-radius:2px;font-size:7.5px;font-style:italic;color:#999;padding:6px 6px}
.search svg{position:absolute;right:6px;top:4px}
.brand{left:120px;top:56px;display:flex;align-items:center;gap:7px;white-space:nowrap}
.brand .mark{width:14px;height:14px;border-radius:50%;background:var(--gold);flex-shrink:0}
.brand .name{font-size:22px;line-height:28px;font-weight:700;color:var(--brand);letter-spacing:.3px}
.slogan{left:139px;top:98px;font-size:8.6px;color:#333;white-space:nowrap}
.nav{left:362px;top:75px;display:flex;gap:21.5px;font-size:8.3px;color:#222;white-space:nowrap}
.slider{left:118px;top:122px;width:600px;height:298px;background:#fff;border:1px solid #e2e2e2;padding:3px}
.slider .photo{width:100%;height:100%;background:linear-gradient(to bottom,#8fb1d8 0%,#cfdff0 40%,#4e6e3c 62%,#2d4520 100%)}
.slider .arrow{top:150px;width:19px;height:19px;border-radius:50%;background:#fff;opacity:.9;display:flex;align-items:center;justify-content:center}
h2{font-weight:400;color:var(--ink)}
.welcome{left:119px;top:431px;font-size:14px}
.rule{height:1px;background:var(--rule)}
.intro{left:119px;top:471px;width:598px;font-size:7px;line-height:13.2px;text-align:justify;color:#333}
.recent{left:119px;top:549px;font-size:15px}
.recent span{color:var(--gold)}
.card{width:187px}
.card .pic{height:101px;position:relative}
.card .date{position:absolute;right:0;top:0;width:33px;height:78px;background:var(--gold);color:#fff;text-align:center;font-family:'Roboto',sans-serif}
.card .date b{display:block;font-size:16px;font-weight:400;margin-top:10px}
.card .date i{font-style:normal;font-size:9px;display:block;margin-top:9px}
.card .cm{position:absolute;right:0;top:78px;width:33px;height:23px;background:#555;display:flex;align-items:center;justify-content:center}
.card h3{font-size:11px;font-weight:400;color:#333;margin-top:14px;white-space:nowrap}
.card p{font-size:7px;line-height:13px;text-align:justify;margin-top:9px;color:#444}
.card .more{font-size:7px;font-weight:700;color:#222;margin-top:8px;display:flex;align-items:center;gap:6px;padding-left:2px}
.more .dot{width:8px;height:8px;border-radius:50%;background:var(--orange)}
.quick{left:540px;top:552px;width:177px;height:245px;border:1px solid #e2e2e2;border-radius:3px;overflow:hidden}
.quick h4{height:33px;font-family:'Roboto',sans-serif;font-weight:400;font-size:14px;color:#111;padding:9px 11px;background:#fff}
.quick form{background:var(--teal);height:212px;padding:11px 11px}
.field{height:22px;background:#fff;border:1px solid #ccc;font-size:7.2px;color:#666;padding:6px 8px;margin-bottom:8px;font-family:'Roboto',sans-serif}
.field.msg{height:40px}
.send{margin:6px auto 0;width:52px;height:24px;border-radius:12px;background:var(--gold-btn);color:#fff;font-weight:700;font-size:11px;text-align:center;line-height:24px}
.news-title{left:119px;top:819px;font-size:11px}
.pager{top:820px;width:13px;height:13px;border:1px solid #ccc;border-radius:50%;display:flex;align-items:center;justify-content:center}
.news{width:298px;height:112px;display:flex;gap:12px}
.news .frame{width:144px;flex-shrink:0;height:112px;border:1px solid #e2e2e2;padding:4px;background:#fff}
.news .frame div{width:100%;height:100%}
.news h3{font-size:10px;font-weight:400;color:#222;padding-bottom:6px;border-bottom:1px solid var(--rule);white-space:nowrap}
.news .when{font-size:7px;color:#333;margin-top:8px;display:flex;gap:7px;align-items:center}
.news p{font-size:7px;line-height:13.2px;text-align:justify;margin-top:8px;color:#333}
.footer{left:0;top:993px;width:836px;height:166px;background:var(--footer)}
.footer h5{font-weight:400;font-size:11px;color:#e0e0e0;position:absolute}
.pages{left:120px;font-size:7px;color:var(--footer-text);line-height:19px;position:absolute}
.touch{position:absolute;font-size:8px;color:var(--footer-text);line-height:13px}
.player{left:505px;top:40px;width:213px;height:51px;border:1px solid #222;border-radius:2px;background:linear-gradient(#3e3e3e,#2a2a2a)}
.player .btn{position:absolute;top:28px;width:17px;height:17px;border-radius:50%;background:#555;border:1px solid #333}
.base{left:0;top:1159px;width:836px;height:41px;background:var(--footer-base)}
.base .copy{right:119px;top:15px;font-size:7.5px;color:#ccc}
</style>
</head>
<body>

<div class="abs topbar">
  <div class="abs call">
    <svg width="10" height="9" viewBox="0 0 10 9"><path d="M1 3C1 1 3 1 5 1S9 1 9 3L7 3 7 2 3 2 3 3ZM2 4H8L9 8H1Z" fill="#ddd"/></svg>
    Call Us Free: 0508 447 300
  </div>
  <div class="abs search">Search
    <svg width="12" height="12" viewBox="0 0 12 12"><circle cx="5" cy="5" r="3.6" fill="none" stroke="#777" stroke-width="1.4"/><path d="M7.6 7.6 11 11" stroke="#777" stroke-width="1.8"/></svg>
  </div>
</div>

<div class="abs brand"><span class="mark"></span><span class="name">Tall Fern Trees</span></div>
<div class="abs slogan">Great Looking Trees that Grow Well</div>
<nav class="abs nav"><span>HOME</span><span>ABOUT US</span><span>TREE GALLERY</span><span>PROJECTS</span><span>CATALOGUE</span><span>CONTACT</span></nav>

<div class="abs slider">
  <div class="photo" role="img" aria-label="Banner photo of tall trees under a cloudy blue sky with white birds flying across"></div>
  <div class="abs arrow" style="left:22px"><svg width="7" height="7"><path d="M5 1 2 3.5 5 6" stroke="#666" fill="none" stroke-width="1.4"/></svg></div>
  <div class="abs arrow" style="right:22px"><svg width="7" height="7"><path d="M2 1 5 3.5 2 6" stroke="#666" fill="none" stroke-width="1.4"/></svg></div>
</div>

<h2 class="abs welcome">Welcome to Tall Fern Trees</h2>
<div class="abs rule" style="left:119px;top:458px;width:598px"></div>
<p class="abs intro">Most are available for immediate delivery New Zealand wide. All trees are grown in 100% Southland peat- a natural soil medium. They grow better and are lighter and easier to transport. Your tree requirements can be in large numbers of even grades. We offer contract growing of trees in advance for future projects. You can trust Tall Fern Trees to deliver the goods and exceed your expectations. Most are available for immediate delivery New Zealand wide. All trees are grown in 100% Southland peat- a natural soil medium. They grow better and are lighter and easier to transport. Your tree requirements can be in large numbers of even grades. We offer contract growing of trees in advance for future projects. You can trust Tall Fern Trees to deliver the goods and exceed your expectations.</p>

<h2 class="abs recent">Recent <span>Projects</span></h2>
<div class="abs rule" style="left:119px;top:578px;width:402px"></div>

<article class="abs card" style="left:120px;top:593px">
  <div class="pic" role="img" aria-label="Photo of a modern arena building with young trees" style="background:linear-gradient(#7fa7d6,#c9d6e0 45%,#8a8f88 75%,#6d6f6a)">
    <div class="date"><b>15</b><i>Jan</i></div>
    <div class="cm"><svg width="11" height="9"><ellipse cx="5.5" cy="4" rx="5" ry="3.5" fill="#fff"/></svg></div>
  </div>
  <h3>Harbourside Arena &amp; Campus</h3>
  <p>A prestigious project with scale and new edge architecture This project included plantings of hardy trees such as Liquidambar, Betula, Fraxinus and Quercus specimen...</p>
  <div class="more">Read More <span class="dot"></span></div>
</article>

<article class="abs card" style="left:333px;top:593px">
  <div class="pic" role="img" aria-label="Photo of a lakeside village house below rocky mountains" style="background:linear-gradient(#8fb0d8,#b6b2aa 40%,#6b7355 70%,#4f7a2c)">
    <div class="date"><b>15</b><i>Jan</i></div>
    <div class="cm"><svg width="11" height="9"><ellipse cx="5.5" cy="4" rx="5" ry="3.5" fill="#fff"/></svg></div>
  </div>
  <h3>Kestrel Ridge Village, Lakeview</h3>
  <p>Lakeside Village with designed with privacy &amp; class Griselinia littoralis – NZ Native Broadleaf provide excellent screening in this Lakeview development, they also add..</p>
  <div class="more">Read More <span class="dot"></span></div>
</article>

<aside class="abs quick">
  <h4>Quick Contact</h4>
  <form>
    <div class="field">Your Name (required)</div>
    <div class="field">Phone Number</div>
    <div class="field">Your Email (required)</div>
    <div class="field">Subject</div>
    <div class="field msg">Your Message</div>
    <div class="send">send</div>
  </form>
</aside>

<h2 class="abs news-title">Latest News</h2>
<div class="abs pager" style="left:686px"><svg width="5" height="6"><path d="M4 .5 1 3 4 5.5" stroke="#777" fill="none"/></svg></div>
<div class="abs pager" style="left:704px"><svg width="5" height="6"><path d="M1 .5 4 3 1 5.5" stroke="#777" fill="none"/></svg></div>
<div class="abs rule" style="left:119px;top:843px;width:598px"></div>

<article class="abs news" style="left:119px;top:856px">
  <div class="frame"><div role="img" aria-label="Photo of a spreading elm tree with deep green foliage" style="background:linear-gradient(#3f7a22,#5f9a35 60%,#c9c6b8)"></div></div>
  <div>
    <h3>Horizontal or Spreading Elm</h3>
    <div class="when"><svg width="8" height="8"><rect x=".5" y="1.5" width="7" height="6" fill="none" stroke="#aaa"/><path d="M.5 3.5H7.5" stroke="#aaa"/></svg>December 18, 2011</div>
    <p>Horizontal or Spreading Elm (also known) Ulmus glabra 'Horizontalis' is an excellent hardy shade tree with wide spreading canopy and deep green foliage. Lime green blossom in spring.</p>
  </div>
</article>
<article class="abs news" style="left:424px;top:856px">
  <div class="frame"><div role="img" aria-label="Photo of a gravel road lined with tall trees under blue sky" style="background:linear-gradient(#2f5fa8,#a9c0dc 45%,#7a7a4a 70%,#8a7a5a)"></div></div>
  <div>
    <h3>Horizontal or Spreading Elm</h3>
    <div class="when"><svg width="8" height="8"><rect x=".5" y="1.5" width="7" height="6" fill="none" stroke="#aaa"/><path d="M.5 3.5H7.5" stroke="#aaa"/></svg>December 18, 2011</div>
    <p>Horizontal or Spreading Elm (also known) Ulmus glabra 'Horizontalis' is an excellent hardy shade tree with wide spreading canopy and deep green foliage. Lime green blossom in spring.</p>
  </div>
</article>

<footer class="abs footer">
  <h5 style="left:120px;top:13px">PAGES</h5>
  <div class="pages" style="top:43px">ABOUT US<br>BLOG<br>CATALOGUE<br>CONTACT<br>PRODUCT GALLERIES<br>PROJECTS</div>
  <h5 style="left:281px;top:13px">GET IN TOUCH</h5>
  <svg class="abs" style="left:281px;top:43px" width="11" height="17"><path d="M5.5 16C2 10 .5 8 .5 5.5a5 5 0 0 1 10 0C10.5 8 9 10 5.5 16Z" fill="#222"/><circle cx="5.5" cy="5.5" r="2" fill="#777"/></svg>
  <div class="touch" style="left:304px;top:44px;width:150px">58 Kerrow Lane, Invercargill 9812</div>
  <svg class="abs" style="left:282px;top:83px" width="11" height="18"><rect x=".5" y=".5" width="10" height="17" rx="1.5" fill="#222"/><rect x="2" y="3" width="7" height="10" fill="#666"/></svg>
  <div class="touch" style="left:306px;top:87px">Toll free: 0508 447 300</div>
  <svg class="abs" style="left:280px;top:121px" width="16" height="11"><rect width="16" height="11" fill="#222"/><path d="M0 0 8 6 16 0" stroke="#777" fill="none"/></svg>
  <div class="touch" style="left:306px;top:120px">Email: sales@tallfernwood.co.nz</div>

  <div class="abs player" role="group" aria-label="Birdsong audio player">
    <div class="abs" style="left:7px;top:10px;width:198px;height:4px;border-radius:2px;background:#222"></div>
    <div class="abs" style="left:7px;top:10px;width:92px;height:4px;border-radius:2px;background:#1f8d7a"></div>
    <div class="abs" style="left:95px;top:8px;width:8px;height:8px;border-radius:50%;background:#ddd"></div>
    <div class="btn" style="left:8px"></div>
    <svg class="abs" style="left:12px;top:32px" width="9" height="9"><path d="M1 8 8 1M5 1H8V4M1 5V8H4" stroke="#aaa" fill="none"/></svg>
    <div class="btn" style="left:73px"></div>
    <svg class="abs" style="left:77px;top:33px" width="9" height="7"><path d="M1 0V7M9 0 5 3.5 9 7ZM5 0 1 3.5 5 7Z" fill="#bbb" stroke="#bbb" stroke-width=".6"/></svg>
    <div class="abs" style="left:96px;top:26px;width:21px;height:21px;border-radius:50%;background:#5c5c5c;border:1px solid #333"></div>
    <svg class="abs" style="left:103px;top:31px" width="8" height="10"><path d="M0 0 8 5 0 10Z" fill="#ccc"/></svg>
    <div class="btn" style="left:122px"></div>
    <svg class="abs" style="left:126px;top:33px" width="9" height="7"><path d="M8 0V7M0 0 4 3.5 0 7ZM4 0 8 3.5 4 7Z" fill="#bbb" stroke="#bbb" stroke-width=".6"/></svg>
    <div class="btn" style="left:186px"></div>
    <svg class="abs" style="left:190px;top:32px" width="9" height="9"><path d="M1 3H3L6 1V8L3 6H1Z" fill="#aaa"/></svg>
  </div>
</footer>

<div class="abs base">
  <div class="abs copy">Copyright@2014 Tall Fern Trees. All Right Reserved</div>
</div>

</body>
</html>
```